Ember/Tide E liquid Menu flyer

Lunvel Mist is a premium E-liquid manufacturing company. This Flyer should be Dual sided with each side dedicated to one of our two juice lines, Ember and Tide. I've included our corporate logo, and Line logo files, along with the source images we used for the logos and PDF copys of our very rough menus with flavor descriptions. All of the flavor information will need to be included for each flavor, if you would like to fluff out the descriptions a bit, even better. I've also included PSD files for the labels so that you can retrieve the fonts and effects we used as well. The following information should also be available at the bottom in fine but readable printKarmic Vaporwww.lunvelmist.com864-873-9117

Target Market(s)

Vapers age 18+

Industry/Entity Type

It Company

Font styles to use
Serif
Sans Serif
Decorative
Script

Requirements
Must have
• Company logo, juice line logo (Ember on one side, Tide on the other) flavor names, and descriptions, website and telephone info.
Nice to have
• I'm not super picky, it just needs to incorporate all of the information and be appealing to the eye.
Should not have
• Any childish cartoonish imagery

```html
<!DOCTYPE html>
<html lang="en">
<head>
<meta charset="utf-8">
<title>Tide – Lunvel Mist Flavor Menu</title>
<link rel="stylesheet" href="https://fonts.googleapis.com/css2?family=Lato:wght@400;700;900&family=Exo+2:ital,wght@1,900&display=swap">
<style>
  :root {
    --page-bg: #d9d9d6;
    --paper: #ffffff;
    --ink: #141414;
    --purple: #6a0dad;
    --mist: #e6e6e6;
    --wall-warm: #b86a3a;
    --wall-gold: #b39433;
    --wall-red: #b8463a;
    --wall-teal: #6fb3c9;
    --wall-slate: #4d5a5c;
    --wall-dark: #3a3231;
  }
  * { box-sizing: border-box; margin: 0; padding: 0; }
  html, body {
    width: 1200px; height: 900px; overflow: hidden;
    background: var(--page-bg);
  }
  .flyer {
    position: absolute; left: 50px; top: 25px;
    width: 1100px; height: 850px;
    background: var(--paper);
    overflow: hidden;
    box-shadow: 0 8px 24px rgba(0,0,0,.25);
    font-family: "Lato", sans-serif;
    color: var(--ink);
  }
  .wall-top {
    position: absolute; left: 0; top: 0; width: 100%; height: 300px;
    background:
      linear-gradient(180deg, rgba(255,255,255,0) 50%, var(--mist) 80%, var(--paper) 100%),
      linear-gradient(90deg, var(--wall-gold) 0%, var(--wall-warm) 22%, var(--wall-red) 45%, var(--wall-slate) 60%, var(--wall-teal) 82%, var(--wall-red) 100%);
  }
  .wall-bottom {
    position: absolute; left: 0; bottom: 0; width: 100%; height: 225px;
    background:
      linear-gradient(0deg, rgba(255,255,255,0) 82%, var(--paper) 100%),
      linear-gradient(90deg, var(--wall-dark) 0%, var(--wall-slate) 25%, var(--wall-warm) 55%, var(--wall-dark) 70%, var(--wall-red) 100%);
  }
  .line-title {
    position: absolute; left: 0; right: 0; top: -18px;
    text-align: center;
    font-family: "Exo 2", sans-serif;
    font-style: italic; font-weight: 900;
    font-size: 250px; line-height: 1.1;
    color: var(--ink);
    -webkit-text-stroke: 3px var(--purple);
    paint-order: stroke fill;
    text-shadow: 4px 5px 0 rgba(0,0,0,.35);
  }
  .menu {
    position: absolute; left: 62px; top: 318px; width: 990px;
    display: grid; grid-template-columns: 534px 456px;
    grid-auto-rows: 105px;
  }
  .flavor-name {
    color: var(--purple); font-weight: 700; font-size: 22px; line-height: 26px;
  }
  .flavor-desc {
    font-size: 21.5px; line-height: 26px; max-width: 440px;
  }
  .brand {
    position: absolute; left: 38px; top: 676px;
    display: flex; align-items: center; gap: 14px;
  }
  .brand-mark {
    width: 84px; height: 84px; border-radius: 50%;
    background: var(--paper); border: 6px solid var(--purple);
  }
  .brand-name {
    background: var(--paper); padding: 6px 16px; border-radius: 6px;
    color: var(--purple); font-weight: 900; font-size: 30px;
  }
  .website {
    position: absolute; left: 443px; top: 667px; width: 612px; height: 44px;
    background: var(--paper); border-radius: 10px;
    display: flex; align-items: center; justify-content: center;
    font-weight: 900; font-style: italic; font-size: 26px; letter-spacing: 9px;
  }
  .phone {
    position: absolute; left: 443px; width: 612px; top: 728px;
    text-align: center;
    font-family: "Exo 2", sans-serif; font-style: italic; font-weight: 900;
    font-size: 52px; letter-spacing: 2px; line-height: 1.2;
    color: var(--paper);
    -webkit-text-stroke: 6px var(--ink);
    paint-order: stroke fill;
    text-shadow: 3px 3px 0 var(--ink);
  }
</style>
</head>
<body>
  <main class="flyer">
    <div class="wall-top" role="img" aria-label="Painted graffiti brick wall texture in gold, red and teal"></div>
    <h1 class="line-title">Tide</h1>

    <section class="menu">
      <article class="flavor">
        <h2 class="flavor-name">Golden Haze</h2>
        <p class="flavor-desc">A fresh spin on a classic, honey glow fans will want to try this one right away!</p>
      </article>
      <article class="flavor">
        <h2 class="flavor-name">Rootstone</h2>
        <p class="flavor-desc">Settle into the ground of every pleasure and savor this soft, rich strawberry shortcake</p>
      </article>
      <article class="flavor">
        <h2 class="flavor-name">Berry Jester</h2>
        <p class="flavor-desc">This take on a bright fruity morning cereal is made for grown-up tastes only!</p>
      </article>
      <article class="flavor">
        <h2 class="flavor-name">Island Pour</h2>
        <p class="flavor-desc">This will carry you to the shore with your favorite blended fruity drink</p>
      </article>
      <article class="flavor">
        <h2 class="flavor-name">Easy Evenings</h2>
        <p class="flavor-desc">Watermelon, kiwi and peach. Built for slow nights and easy evenings.</p>
      </article>
      <article class="flavor">
        <h2 class="flavor-name">Berry Meadow</h2>
        <p class="flavor-desc">Fresh berries and cream all day</p>
      </article>
    </section>

    <div class="wall-bottom" role="img" aria-label="Painted graffiti wall texture in dark slate, rust and red"></div>
    <div class="brand">
      <span class="brand-mark"></span>
      <span class="brand-name">Lunvel Mist</span>
    </div>
    <div class="website">www.lunvelmist.example</div>
    <div class="phone">555-302-4718</div>
  </main>
</body>
</html>
```